I am looking for a flyer design for my upcoming symposium. Here are the details for the flyer and pictures of speakers are attached.

Name of Symposium: Lattice and Pathway Biosciences Symposium, Sponsored by the Corvale Chromatin Institute and the Department of Bioengineering
Date: January 8, 2018
Location: Havergill Auditorium, Tarnby Center for Applied Discovery, 2175 Orchard Terrace Ave, Philadelphia, PA 19127

Reception to follow after the symposium.

Also, please add - Register and upload abstracts for the symposium at www.qzvmrk.com. Registration and abstract submission closes on January 4, 2018.

Keynote Speaker:
Marthe Quillon, Ph.D.
NTVO Director General; Professor, Lyceum of Norvane; Director, Genetics and Developmental Biology at Institut Bramoux
Lyceum of Norvane, NTVO, Institut Bramoux
"Title of talk TBA."

Speakers:
Lena Drewcott, Ph.D.
Assistant Professor of Cell and Developmental Biology
Halvering State University, HMCS
"Title of talk TBA."

Paul Marden, Ph.D.
Assistant Professor of Genetics
"Title of talk TBA."

Ilse Varga, Ph.D.
Professor, Ostrander University
Otto Wenzlau Center for Molecular Medicine
"Title of talk TBA."

Jun Hao, Ph.D.
Professor of Cellular and Molecular Medicine
Coastal Meridian University
"Title of talk TBA."

Wei Lun, Ph.D.
Associate Professor of Pediatrics
The Youth Medical Pavilion of Philadelphia
"Spatial genome re-organization between fetal and adult hematopoietic stem cells."

Mei Zhou, Ph.D.
Professor, Department of Genetics
Ellsworth Medical School
"Title of talk TBA."

```html
<!DOCTYPE html>
<html lang="en">
<head>
<meta charset="utf-8">
<title>Lattice and Pathway Biosciences Symposium</title>
<link rel="stylesheet" href="https://fonts.googleapis.com/css2?family=Montserrat:wght@300;400;600;700;800&family=Playfair+Display:wght@400&display=swap">
<style>
  :root {
    --backdrop: #d6d6d6;
    --paper: #ffffff;
    --teal-deep: #1d4a62;
    --teal-mid: #2b6a82;
    --teal-light: #6aa9c2;
    --navy: #232a3a;
    --red: #c8202c;
    --orange: #e8742a;
    --ink: #2a2f3a;
    --white: #ffffff;
  }
  * { box-sizing: border-box; margin: 0; padding: 0; }
  html, body { width: 1200px; height: 841px; overflow: hidden; }
  body {
    background: var(--backdrop);
    font-family: "Montserrat", Arial, sans-serif;
    color: var(--white);
  }
  .flyer {
    position: absolute;
    left: 330px; top: 38px;
    width: 540px; height: 764px;
    background: var(--paper);
    overflow: hidden;
  }
  .hero-image {
    position: absolute; inset: 0;
    background: radial-gradient(ellipse at 78% 30%, var(--teal-light) 0%, var(--teal-mid) 40%, var(--teal-deep) 80%);
  }
  .header-band {
    position: absolute; left: 0; top: 0;
    width: 330px; height: 118px;
    background: var(--paper);
  }
  .header-band .accent-bar {
    position: absolute; left: 0; top: 30px;
    width: 88px; height: 7px; background: var(--navy);
  }
  .org-mark {
    position: absolute;
    display: flex; align-items: center; gap: 6px;
    font-size: 10px; font-weight: 600; color: var(--navy);
    white-space: nowrap;
  }
  .org-mark .dot { width: 11px; height: 11px; background: var(--navy); flex: none; }
  .org-mark.engineering { left: 20px; top: 80px; }
  .org-mark.institute { left: 150px; top: 52px; color: var(--red); }
  .org-mark.institute .dot { background: var(--red); border-radius: 50%; }

  .url-strip {
    position: absolute; right: 0; top: 150px;
    width: 62px; height: 340px;
    background: var(--paper);
  }
  .url-strip .url-text {
    position: absolute; left: 24px; top: 30px;
    writing-mode: vertical-rl;
    font-size: 10px; letter-spacing: 4px; color: var(--ink);
  }
  .url-strip .url-rule {
    position: absolute; left: 30px; bottom: 20px;
    width: 2px; height: 34px; background: var(--orange);
  }

  .speakers-label {
    position: absolute; left: 336px; top: 92px;
    font-size: 12px; font-weight: 700; text-decoration: underline;
  }
  .speaker {
    position: absolute;
    width: 120px; height: 70px;
  }
  .speaker .portrait {
    position: absolute; left: 0; top: 0;
    width: 32px; height: 32px; border-radius: 50%;
    background: linear-gradient(135deg, #b89684, #5f4a40);
    border: 2px solid var(--white);
    z-index: 1;
  }
  .speaker .caption {
    position: absolute; left: 20px; top: 20px;
    width: 100px; padding: 4px 5px 4px 8px;
    border-radius: 4px;
    font-size: 4.6px; line-height: 1.25;
    z-index: 2;
  }
  .speaker .caption b { display: block; font-size: 5.2px; }
  .speaker.dark .caption { background: var(--navy); }
  .speaker.red .caption { background: var(--red); }

  .date-block {
    position: absolute; left: 36px; top: 150px;
    width: 96px; padding: 10px 0;
    border-top: 1px solid var(--white);
    border-bottom: 1px solid var(--white);
    font-weight: 800; font-size: 28px; line-height: 0.95; text-align: center;
  }
  .sponsor-line {
    position: absolute; left: 146px; top: 182px;
    width: 188px;
    font-size: 11px; font-weight: 300; line-height: 1.3;
  }
  .sponsor-line b { font-weight: 700; }

  .title-bar {
    position: absolute; left: 0;
    background: var(--navy);
    font-family: "Playfair Display", Georgia, serif;
    font-weight: 400;
    font-size: 26px; line-height: 44px; white-space: nowrap;
    padding-right: 16px;
  }
  .title-bar.first { top: 254px; padding-left: 40px; }
  .title-bar.second { top: 306px; padding-left: 30px; }

  .location {
    position: absolute; left: 40px; top: 372px;
    font-size: 12px; line-height: 1.35;
  }
  .location .venue { font-weight: 300; font-size: 17px; }
  .location b { font-weight: 700; }
  .location .rule { width: 36px; height: 1px; background: var(--white); margin-top: 12px; }

  .keynote-portrait {
    position: absolute; left: 248px; top: 450px;
    width: 90px; height: 90px; border-radius: 50%;
    background: linear-gradient(135deg, #c8a493, #6d4f44);
    border: 4px solid var(--red);
  }
  .keynote {
    position: absolute; left: 40px; top: 470px;
    width: 200px;
  }
  .keynote h2 {
    font-size: 16px; font-weight: 700; text-decoration: underline; margin-bottom: 6px;
  }
  .keynote p { font-size: 7.5px; line-height: 1.4; }
  .keynote p b { font-weight: 700; }

  .footer-band {
    position: absolute; left: 0; bottom: 0;
    width: 540px; height: 168px;
    background: var(--navy);
    display: flex; align-items: center; justify-content: center;
    padding-left: 60px;
  }
  .footer-band p {
    font-size: 12.5px; font-weight: 400; line-height: 1.5; text-align: center;
  }
  .footer-notch {
    position: absolute; left: 0; bottom: 0;
    width: 44px; height: 118px; background: var(--paper);
  }
</style>
</head>
<body>
  <article class="flyer">
    <div class="hero-image" role="img" aria-label="Blue molecular backdrop with DNA double helix and hexagon structures"></div>

    <header class="header-band">
      <div class="accent-bar"></div>
      <div class="org-mark institute"><span class="dot"></span>Corvale Chromatin Institute</div>
      <div class="org-mark engineering"><span class="dot"></span>Corvale Engineering</div>
    </header>

    <aside class="url-strip">
      <span class="url-text">WWW.QZVMRK.COM</span>
      <span class="url-rule"></span>
    </aside>

    <h3 class="speakers-label">Speakers:</h3>

    <div class="speaker dark" style="left:340px;top:112px">
      <div class="portrait" role="img" aria-label="Portrait of Lena Drewcott"></div>
      <div class="caption"><b>Lena Drewcott, Ph.D.</b>Assistant Professor of Cell and Developmental Biology, Halvering State University, HMCS<br>"Title of talk TBA."</div>
    </div>
    <div class="speaker red" style="left:343px;top:188px">
      <div class="portrait" role="img" aria-label="Portrait of Paul Marden"></div>
      <div class="caption"><b>Paul Marden, Ph.D.</b>Assistant Professor of Genetics<br>"Title of talk TBA."</div>
    </div>
    <div class="speaker dark" style="left:346px;top:264px">
      <div class="portrait" role="img" aria-label="Portrait of Ilse Varga"></div>
      <div class="caption"><b>Ilse Varga, Ph.D.</b>Professor, Ostrander University, Otto Wenzlau Center for Molecular Medicine<br>"Title of talk TBA."</div>
    </div>
    <div class="speaker red" style="left:349px;top:340px">
      <div class="portrait" role="img" aria-label="Portrait of Jun Hao"></div>
      <div class="caption"><b>Jun Hao, Ph.D.</b>Professor of Cellular and Molecular Medicine, Coastal Meridian University<br>"Title of talk TBA."</div>
    </div>
    <div class="speaker dark" style="left:352px;top:416px">
      <div class="portrait" role="img" aria-label="Portrait of Wei Lun"></div>
      <div class="caption"><b>Wei Lun, Ph.D.</b>Associate Professor of Pediatrics, The Youth Medical Pavilion of Philadelphia<br>"Spatial genome re-organization between fetal and adult hematopoietic stem cells."</div>
    </div>
    <div class="speaker red" style="left:355px;top:492px">
      <div class="portrait" role="img" aria-label="Portrait of Mei Zhou"></div>
      <div class="caption"><b>Mei Zhou, Ph.D.</b>Professor, Department of Genetics, Ellsworth Medical School<br>"Title of talk TBA."</div>
    </div>

    <div class="date-block">08<br>Jan<br>18</div>
    <p class="sponsor-line">Sponsored by the <b>Corvale Chromatin Institute</b> and the <b>Department of Bioengineering</b></p>

    <h1>
      <span class="title-bar first">Lattice and Pathway</span>
      <span class="title-bar second">Biosciences Symposium</span>
    </h1>

    <div class="location">
      <div class="venue">Location: Havergill Auditorium,</div>
      <b>Tarnby Center for Applied Discovery, 2175<br>Orchard Terrace Ave, Philadelphia, PA 19127</b>
      <div class="rule"></div>
    </div>

    <div class="keynote-portrait" role="img" aria-label="Portrait of keynote speaker Marthe Quillon"></div>
    <section class="keynote">
      <h2>Keynote Speaker:</h2>
      <p><b>Marthe Quillon, Ph.D.</b><br>NTVO Director General; Professor, Lyceum of Norvane; Director, Genetics and Developmental Biology at Institut Bramoux<br>Lyceum of Norvane, NTVO, Institut Bramoux<br>"Title of talk TBA."</p>
    </section>

    <footer class="footer-band">
      <p>Register and upload abstracts for the symposium at www.qzvmrk.com.<br>Registration and abstract submission closes on January 4, 2018.</p>
    </footer>
    <div class="footer-notch"></div>
  </article>
</body>
</html>
```